ALL TEXT Social Media Graphics

We are looking for a series of social media graphics for Instagram (new size: 4:5 (1080 x 1350 pixels) ratio that are ALL TEXT. We want the following quotes below on each graphic; one quote per graphic. AND, In very small letters at the bottom of each graphic, add @PaulaWrenLive
The look and feel of these graphics should be complimentary to the color palette attached below; but keep them simple. But the design is up to you; at the end of this document, I provided various samples of all text graphics that I like as examples.
The Quotes are in the attached WORD document
women trying to lose weight

```html
<!DOCTYPE html>
<html lang="en">
<head>
<meta charset="utf-8">
<title>Glow Girl Summer Slimdown – Instagram Text Series</title>
<link href="https://fonts.googleapis.com/css2?family=Bebas+Neue&family=Bodoni+Moda:ital@1&family=Noto+Sans:wght@400;700&display=swap" rel="stylesheet">
<style>
  :root {
    --backdrop: #fcc0e0;
    --card: #ffffff;
    --berry: #b3175a;
    --rose: #ee5d91;
    --ink: #111111;
  }
  * { margin: 0; padding: 0; box-sizing: border-box; }
  html, body { width: 1200px; height: 933px; overflow: hidden; }
  body { background: var(--backdrop); position: relative; font-family: "Noto Sans", sans-serif; color: var(--ink); }

  .post { position: absolute; width: 288px; height: 360px; background: var(--card); }
  .post--1 { left: 99px;  top: 74px; }
  .post--2 { left: 456px; top: 74px; }
  .post--3 { left: 813px; top: 74px; }
  .post--4 { left: 99px;  top: 500px; }
  .post--5 { left: 456px; top: 500px; }

  .post > * { position: absolute; white-space: nowrap; }

  .headline { font-family: "Bebas Neue", sans-serif; color: var(--berry); font-weight: 400; letter-spacing: 0.3px; }
  .headline .accent, .accent { color: var(--rose); }

  .body-copy { font-size: 15px; line-height: 19.5px; letter-spacing: 0.4px; font-weight: 400; }
  .lead { font-size: 18px; font-weight: 700; letter-spacing: 0.5px; }

  .cta { font-size: 20px; font-weight: 700; letter-spacing: 0.6px; line-height: 1; display: flex; align-items: baseline; gap: 5px; }
  .cta .keyword { font-family: "Bebas Neue", sans-serif; font-weight: 400; font-size: 31px; color: var(--berry); letter-spacing: 0.5px; }

  .script { font-family: "Bodoni Moda", serif; font-style: italic; color: var(--rose); font-size: 19px; line-height: 23px; }

  .handle { font-size: 12px; letter-spacing: 0.3px; }

  /* card 1 */
  .post--1 .headline { left: 16px; top: 14px; font-size: 30px; line-height: 34px; }
  .post--1 .body-copy { left: 16px; top: 186px; }
  .post--1 .cta { left: 16px; top: 233px; }
  .post--1 .script { left: 16px; top: 270px; }
  .post--1 .handle { left: 15px; top: 325px; }

  /* card 2 */
  .post--2 .headline { left: 14px; top: 20px; font-size: 37px; line-height: 38px; }
  .post--2 .body-copy { left: 14px; top: 186px; line-height: 18px; }
  .post--2 .cta { left: 14px; top: 251px; }
  .post--2 .handle { left: 14px; top: 305px; }

  /* card 3 */
  .post--3 .headline { left: 11px; top: 28px; font-size: 35px; line-height: 36.5px; }
  .post--3 .body-copy { left: 11px; top: 152px; line-height: 20.5px; }
  .post--3 .cta { left: 11px; top: 226px; }
  .post--3 .script { left: 11px; top: 263px; }
  .post--3 .handle { left: 11px; top: 310px; }

  /* card 4 */
  .post--4 .headline { left: 14px; top: 31px; font-size: 34px; line-height: 38px; }
  .post--4 .body-copy { left: 14px; top: 188px; line-height: 21px; }
  .post--4 .cta { left: 14px; top: 241px; }
  .post--4 .handle { left: 14px; top: 296px; }

  /* card 5 */
  .post--5 .headline { left: 15px; top: 23px; font-size: 39px; line-height: 38px; }
  .post--5 .lead { left: 15px; top: 148px; }
  .post--5 .lead .accent { font-weight: 700; }
  .post--5 .body-copy { left: 15px; top: 185px; line-height: 21px; }
  .post--5 .cta { left: 15px; top: 258px; }
  .post--5 .handle { left: 15px; top: 314px; }
</style>
</head>
<body>

<section class="post post--1">
  <h2 class="headline">Nothing feels<br>better than<br>seeing that<br>scale drop week<br>after week.</h2>
  <p class="body-copy">Let’s lose up to 30 pounds<br>this summer–together.</p>
  <p class="cta">Comment <span class="keyword">“SUMMER”</span></p>
  <p class="script">to join the Glow Girl<br>Summer Slimdown!</p>
  <p class="handle">@PaulaWrenLive</p>
</section>

<section class="post post--2">
  <h2 class="headline">You’ve got<br><span class="accent">8 weeks</span> and<br>the perfect plan<br>to drop <span class="accent">30 pounds.</span></h2>
  <p class="body-copy">Let’s get snatched<br>this summer with the<br>Glow Girl Summer Slimdown.</p>
  <p class="cta">Comment <span class="keyword">“SUMMER”!</span></p>
  <p class="handle">@PaulaWrenLive</p>
</section>

<section class="post post--3">
  <h2 class="headline">Snatched waist,<br>flat tummy,<br>30 pounds lighter –</h2>
  <p class="body-copy">that’s what the Glow Girl<br>Summer Slimdown Challenge<br>delivers.</p>
  <p class="cta">Comment <span class="keyword">“GLOW GIRL”!</span></p>
  <p class="script">to get the plan</p>
  <p class="handle">@PaulaWrenLive</p>
</section>

<section class="post post--4">
  <h2 class="headline"><span class="accent">Sis,</span> we’re dropping<br>belly flat and<br>saying goodbye to<br>stubborn pounds</h2>
  <p class="body-copy">Join the Glow Girl<br>Summer Slimdown–</p>
  <p class="cta">Comment <span class="keyword">“SUMMER”!</span></p>
  <p class="handle">@PaulaWrenLive</p>
</section>

<section class="post post--5">
  <h2 class="headline">Don’t wait ‘til<br>next summer<br>to get right.</h2>
  <p class="lead">The time is <span class="accent">NOW.</span></p>
  <p class="body-copy">Drop 30 pounds<br>with the Glow Girl<br>Summer Slimdown.</p>
  <p class="cta">Comment <span class="keyword">“SUMMER”!</span></p>
  <p class="handle">@PaulaWrenLive</p>
</section>

</body>
</html>
```